We need to design Labels of one of Our Brand BrivaLune Lotion.

The purpose of this product is to keep mosquitoes away.
There are 3 variants of this lotion. So we need 3 designs for the product. These variants details are mentioned below:

1) Mosquito Repellent Lotion with Lavender Fragrance.
2) Mosquito Repellent Lotion with Natural Ingredients.
3) Mosquito Repellent Lotion for kids.

Kindly note the bottle will be WHITE for all the variants. Cap will of the bottle will be with accordance to the color of label. In the picture it is red just for presentation.

Kindly share design of Repellent Lotion with Lavendar Fragrance initially and if we give your positive feedback, then you may add further variants of the design.

The bottle shape is attached along with keylines. Also attaching logo. If there is any other option for logo, you can suggest which we would probably keep our existing logo.

Target Market(s)

B+, B, C+

Industry/Entity Type

Product

Colors
a54499
6b449b

Requirements
Must have
• Mosquito
• 100ml
Nice to have
• Purple color as background
Should not have
• Lavendar flower

```html
<!DOCTYPE html>
<html lang="en">
<head>
<meta charset="utf-8">
<title>BrivaLune Mosquito Repellent Lotion – Lavender Label</title>
<link rel="stylesheet" href="https://fonts.googleapis.com/css2?family=Anton&family=Oswald:wght@500;700&display=swap">
<style>
  :root{
    --stage-light:#f4f4f4;
    --stage-mid:#e4e4e4;
    --label-purple:#a54499;
    --label-violet:#6b449b;
    --label-deep:#4e2f7e;
    --banner-blue:#2f8fd4;
    --banner-teal:#1fb2d8;
    --badge-blue:#1e6fc0;
    --ink-white:#ffffff;
    --stop-red:#e3141b;
  }
  html,body{margin:0;padding:0;overflow:hidden;}
  body{
    width:1200px;height:1199px;
    background:radial-gradient(ellipse at 50% 10%,var(--stage-light) 0%,var(--stage-mid) 75%);
    position:relative;
  }
  .label{
    position:absolute;left:390px;top:200px;width:420px;height:780px;
    filter:drop-shadow(0 6px 10px rgba(0,0,0,.18));
  }
  .brand-name{font-family:"Anton",sans-serif;fill:var(--ink-white);}
  .product-type{font-family:"Oswald",sans-serif;font-weight:700;fill:var(--ink-white);}
  .with-word{font-family:"Anton",sans-serif;fill:var(--label-purple);}
  .fragrance{font-family:"Oswald",sans-serif;font-weight:700;fill:var(--ink-white);}
  .badge-text{font-family:"Oswald",sans-serif;font-weight:700;fill:var(--ink-white);}
  .volume{font-family:"Oswald",sans-serif;font-weight:700;fill:var(--ink-white);}
</style>
</head>
<body>
<svg class="label" viewBox="0 0 140 260" xmlns="http://www.w3.org/2000/svg" aria-label="BrivaLune mosquito repellent lotion label with lavender fragrance">
  <defs>
    <linearGradient id="labelFill" x1="0" y1="0" x2="1" y2="1">
      <stop offset="0" stop-color="var(--label-violet)"/>
      <stop offset=".55" stop-color="var(--label-purple)"/>
      <stop offset="1" stop-color="var(--label-violet)"/>
    </linearGradient>
    <linearGradient id="bannerFill" x1="0" y1="0" x2="1" y2="0">
      <stop offset="0" stop-color="var(--banner-blue)"/>
      <stop offset="1" stop-color="var(--banner-teal)"/>
    </linearGradient>
    <linearGradient id="sceneFill" x1="0" y1="0" x2="0" y2="1">
      <stop offset="0" stop-color="#8a4fa8"/>
      <stop offset="1" stop-color="#6a3d93"/>
    </linearGradient>
    <clipPath id="labelClip">
      <path d="M2,4 Q70,-2 138,2 C134,60 146,100 124,140 C116,170 130,220 132,250 Q70,262 8,252 C12,220 26,180 18,140 C2,110 6,60 2,4 Z"/>
    </clipPath>
  </defs>

  <path class="label-shape" d="M2,4 Q70,-2 138,2 C134,60 146,100 124,140 C116,170 130,220 132,250 Q70,262 8,252 C12,220 26,180 18,140 C2,110 6,60 2,4 Z" fill="url(#labelFill)"/>

  <g clip-path="url(#labelClip)">
    <rect class="room-scene" role="img" aria-label="Soft purple home interior backdrop" x="0" y="160" width="140" height="100" fill="url(#sceneFill)" opacity=".85"/>
  </g>

  <polygon class="brand-banner" points="14,22 128,12 126,74 16,82" fill="url(#bannerFill)"/>

  <ellipse class="new-badge" cx="41" cy="21" rx="15" ry="9" fill="var(--badge-blue)" stroke="var(--ink-white)" stroke-width="1"/>
  <text class="badge-text" x="41" y="24.5" font-size="9" text-anchor="middle">NEW</text>

  <text class="brand-name" x="70" y="63" font-size="24" text-anchor="middle" textLength="104" lengthAdjust="spacingAndGlyphs">BrivaLune</text>

  <text class="product-type" x="70" y="101" font-size="11" text-anchor="middle" letter-spacing="2">MOSQUITO</text>
  <text class="product-type" x="70" y="111" font-size="5.5" text-anchor="middle" letter-spacing=".6">REPELLENT LOTION</text>

  <polygon class="with-band" points="18,124 122,118 120,148 20,154" fill="var(--ink-white)"/>
  <text class="with-word" x="22" y="149" font-size="22" textLength="48" lengthAdjust="spacingAndGlyphs">WITH</text>
  <polygon class="fragrance-tag" points="72,124 120,120 118,146 72,149" fill="var(--label-purple)"/>
  <text class="fragrance" x="75" y="134" font-size="9" textLength="42" lengthAdjust="spacingAndGlyphs">LAVENDER</text>
  <text class="fragrance" x="75" y="144" font-size="9" textLength="42" lengthAdjust="spacingAndGlyphs">FRAGRANCE</text>

  <g class="no-mosquito-icon">
    <circle cx="75" cy="190" r="14" fill="var(--ink-white)" opacity=".25"/>
    <circle role="img" aria-label="Mosquito illustration" cx="75" cy="190" r="9" fill="#d9c9e6" opacity=".7"/>
    <circle cx="75" cy="190" r="14" fill="none" stroke="var(--stop-red)" stroke-width="3"/>
    <line x1="65" y1="200" x2="85" y2="180" stroke="var(--stop-red)" stroke-width="3"/>
  </g>

  <rect class="volume-box" x="48" y="231" width="50" height="15" fill="var(--label-deep)"/>
  <text class="volume" x="73" y="242.5" font-size="10" text-anchor="middle">100ml</text>
</svg>
</body>
</html>
```